Halvern Dental website redesign

We need a redesign for a website: myhalverndental.com.

I already created a video going over what exactly is needed in the design.

See Video here: https://files.quorvane.com/file/d/8xKpQ2mWn4TzLrV7bHsYcE3jFuGaD6oN1/view?usp=sharing

Google Slide shown in Video: https://slides.quorvane.com/presentation/d/7RtW2yQnXbVc4LmPz9KsHdJf3GaE8oUi6TeYqNvB5wZx/edit?usp=sharing
Updates

Holidays in India so we did not get enough design entries or quality.

Target Market(s)

Dentistry

Industry/Entity Type

Dentistry

Number of Pages Required

1 page

Colors
0094D4
00A9DD
6FCCEA
C7EBF8
E9F6FB
00AB8E
00BBA5
67D7C9
C6EFE9
E9F9F6

Requirements
Must have
• See 13 min video link in description - shows what to do.

```html
<!DOCTYPE html>
<html lang="en">
<head>
<meta charset="utf-8">
<title>Halvern Dental — Home</title>
<link href="https://fonts.googleapis.com/css2?family=Montserrat:wght@300;400;500;600;800;900&family=Lato:wght@400;700&display=swap" rel="stylesheet">
<style>
:root{
  --green:#0aa58a;
  --green-dark:#07907a;
  --navy:#2d3183;
  --red:#e0343f;
  --ink:#4a4f6a;
  --muted:#7a7f95;
  --paper:#ffffff;
  --pale:#edf5fd;
  --lavender:#b9addf;
  --violet:#6f63b8;
  --skin:#d9c8bd;
}
*{box-sizing:border-box;margin:0;padding:0}
html,body{width:1200px;height:853px;overflow:hidden;background:var(--paper)}
body{position:relative;font-family:"Lato",sans-serif;color:var(--ink)}
.topbar{position:absolute;left:0;top:0;width:1200px;height:28px;background:var(--green);color:#fff;
  display:flex;align-items:center;padding:0 40px;font-size:10px;font-family:"Montserrat",sans-serif}
.topbar .hours{flex:1}
.topbar .contact{display:flex;gap:28px;align-items:center}
.emergency{background:var(--red);color:#fff;border-radius:3px;padding:4px 14px;font-weight:600;font-size:10px}
.nav{position:absolute;left:0;top:28px;width:1200px;height:56px;display:flex;align-items:center;padding:0 40px}
.brand{display:flex;align-items:center;gap:8px;font-family:"Montserrat",sans-serif;font-weight:600;font-size:20px;color:var(--green);flex:1}
.brand .dot{width:12px;height:12px;border-radius:50%;background:var(--red)}
.nav ul{list-style:none;display:flex;gap:34px;font-family:"Montserrat",sans-serif;font-size:11px;letter-spacing:1.5px;color:var(--navy);font-weight:500}
.hero{position:absolute;left:0;top:84px;width:1200px;height:300px}
.hero-band{position:absolute;left:0;top:150px;width:1200px;height:150px;background:var(--green)}
.hero h1{position:absolute;left:60px;top:24px;font-family:"Montserrat",sans-serif;font-weight:900;font-size:46px;line-height:.98;letter-spacing:.5px}
.hero h1 .g{color:var(--green);display:block}
.hero h1 .n{color:var(--navy);display:block}
.hero .tag{position:absolute;left:60px;top:184px;font-family:"Montserrat",sans-serif;font-weight:400;font-size:24px;line-height:1.15;color:#fff}
.btn{position:absolute;left:60px;top:250px;background:#fff;color:var(--navy);font-family:"Montserrat",sans-serif;font-weight:600;font-size:13px;padding:12px 34px;border-radius:2px}
.hero-art{position:absolute;left:560px;top:8px;width:600px;height:280px;border-radius:4px;
  background:linear-gradient(135deg,#e3ddf6 0%,var(--lavender) 55%,var(--violet) 100%)}
.about{position:absolute;left:0;top:384px;width:1200px;height:216px}
.about-card{position:absolute;left:60px;top:20px;width:560px;height:190px;background:#fff;box-shadow:0 6px 24px rgba(40,50,90,.13);padding:22px 30px}
.eyebrow{font-family:"Montserrat",sans-serif;font-size:9px;letter-spacing:1.5px;color:var(--red);font-weight:600;text-transform:uppercase}
.about-card h2{font-family:"Montserrat",sans-serif;font-weight:300;font-size:26px;color:var(--navy);margin:4px 0 10px}
.about-card p{font-size:10.5px;line-height:1.55;color:var(--muted);margin-bottom:6px}
.about-block{position:absolute;left:700px;top:40px;width:460px;height:170px;background:var(--green)}
.about-photo{position:absolute;left:660px;top:0;width:460px;height:190px;background:linear-gradient(135deg,#f3f3f5,#d7dbe6 60%,var(--skin))}
.lower{position:absolute;left:0;top:600px;width:1200px;height:225px;background:var(--pale)}
.services{position:absolute;left:60px;top:18px;width:420px}
.section-title{font-family:"Montserrat",sans-serif;font-weight:300;font-size:22px;color:var(--navy)}
.services p{font-size:10px;line-height:1.55;color:var(--muted);margin:6px 0 12px;width:390px}
.icons{display:flex;gap:34px}
.icon{display:flex;flex-direction:column;align-items:center;gap:6px;font-size:10px;color:var(--navy);font-family:"Montserrat",sans-serif}
.doctors{position:absolute;left:500px;top:18px;width:260px;text-align:center}
.doctors .arch{width:110px;height:120px;margin:8px auto 6px;border-radius:55px 55px 8px 8px;background:var(--green);padding:8px}
.doctors .portrait{width:94px;height:104px;border-radius:48px 48px 6px 6px;background:linear-gradient(160deg,#f5f4f7,#d9d3d0)}
.doctors .name{font-family:"Montserrat",sans-serif;font-size:12px;color:var(--navy);font-weight:500}
.doctors .role{font-size:9px;letter-spacing:1.2px;color:var(--red);text-transform:uppercase}
.info{position:absolute;left:790px;top:18px;width:370px;display:flex;gap:24px}
.info h3{font-family:"Montserrat",sans-serif;font-size:12px;color:var(--navy);font-weight:600;margin-bottom:6px}
.hours-table{font-size:9.5px;color:var(--muted);border-collapse:collapse}
.hours-table td{padding:1.5px 14px 1.5px 0}
.contact-list{font-size:9.5px;line-height:1.6;color:var(--muted);margin-bottom:8px}
.map{width:170px;height:80px;border-radius:3px;background:linear-gradient(135deg,#eef0f3,#d8dde4)}
.footer{position:absolute;left:0;top:825px;width:1200px;height:28px;background:var(--green);color:#fff;font-size:10px;
  font-family:"Montserrat",sans-serif;display:flex;align-items:center;justify-content:center}
</style>
</head>
<body>
<header class="topbar">
  <span class="hours">Mon - Sat 8AM-7PM, Sunday - CLOSED</span>
  <div class="contact">
    <span>(555) 013-2740</span>
    <span>hello@myhalverndental.com</span>
    <span>48 Linden Crest Ave. Marlow Bay, CA 90410</span>
    <span class="emergency">Emergency</span>
  </div>
</header>
<nav class="nav">
  <div class="brand"><span class="dot"></span>Halvern Dental</div>
  <ul><li>ABOUT US</li><li>SERVICES ⌄</li><li>TESTIMONIALS</li><li>FINANCING</li><li>SPECIALS</li><li>BLOG</li></ul>
</nav>
<section class="hero">
  <div class="hero-band"></div>
  <div class="hero-art" role="img" aria-label="Illustration of a dental chair with overhead lamp and equipment"></div>
  <h1><span class="g">CREATING</span><span class="n">HEALTHIER</span><span class="n">SMILES</span></h1>
  <p class="tag">With Advanced Technology<br>and Affordable Treatment</p>
  <a class="btn">Book an Appointment</a>
</section>
<section class="about">
  <div class="about-block"></div>
  <div class="about-photo" role="img" aria-label="Photo of a dentist showing a dental model to a smiling patient"></div>
  <div class="about-card">
    <div class="eyebrow">Dental Practice</div>
    <h2>Your smile is our #1 priority</h2>
    <p>At Halvern Dental, we provide affordable and expert dental solutions. Whether you need a family dentist, a root canal in Marlow Bay or emergency care, we are here for you. We want to keep your teeth healthy inside and out, and we want to get to know you.</p>
    <p>We give every patient the best experience in a calm and friendly setting, with all the options you need to feel at ease.</p>
  </div>
</section>
<section class="lower">
  <div class="services">
    <h2 class="section-title">Services</h2>
    <p>Halvern Dental offers top dental services at a fair price. Our staff take pride in your smile, keep every visit comfortable and explain each step so you can choose the best care.</p>
    <div class="icons">
      <div class="icon"><svg width="40" height="40" viewBox="0 0 40 40"><rect x="4" y="26" width="32" height="8" fill="#c6efe9"/><path d="M10 6c5-3 8 1 10 1s5-4 10-1c4 3 2 12 0 16l-2 12h-3l-2-9h-6l-2 9h-3l-2-12C8 18 6 9 10 6z" fill="none" stroke="#2d3183" stroke-width="2"/></svg>Bridge</div>
      <div class="icon"><svg width="40" height="40" viewBox="0 0 40 40"><rect x="4" y="26" width="32" height="8" fill="#c6efe9"/><path d="M10 10c5-3 8 1 10 1s5-4 10-1c4 3 2 12 0 16l-2 10h-3l-2-8h-6l-2 8h-3l-2-10C8 22 6 13 10 10z" fill="none" stroke="#2d3183" stroke-width="2"/><path d="M26 2l4 4" stroke="#0aa58a" stroke-width="2"/></svg>Extractions</div>
      <div class="icon"><svg width="40" height="40" viewBox="0 0 40 40"><path d="M10 10c5-3 8 1 10 1s5-4 10-1c4 3 2 12 0 16l-2 10h-3l-2-8h-6l-2 8h-3l-2-10C8 22 6 13 10 10z" fill="none" stroke="#2d3183" stroke-width="2"/><circle cx="28" cy="10" r="7" fill="#c6efe9" stroke="#0aa58a" stroke-width="1.5"/></svg>Gum Disease</div>
    </div>
  </div>
  <div class="doctors">
    <div class="eyebrow">The Halvern Dental Team</div>
    <h2 class="section-title">Meet Our Doctors</h2>
    <div class="arch"><div class="portrait" role="img" aria-label="Portrait photo of the lead dentist in a white coat"></div></div>
    <div class="name">Dr. Elena Voss</div>
    <div class="role">Cosmetic Dentist</div>
  </div>
  <div class="info">
    <div>
      <h3>Work Hours</h3>
      <table class="hours-table">
        <tr><td>Monday</td><td>8AM-7PM</td></tr>
        <tr><td>Tuesday</td><td>8AM-7PM</td></tr>
        <tr><td>Wednesday</td><td>8AM-7PM</td></tr>
        <tr><td>Thursday</td><td>8AM-7PM</td></tr>
        <tr><td>Friday</td><td>8AM-7PM</td></tr>
        <tr><td>Saturday</td><td>8AM-7PM</td></tr>
        <tr><td>Sunday</td><td>CLOSED</td></tr>
      </table>
    </div>
    <div>
      <h3>Contact Info</h3>
      <div class="contact-list">(555) 013-2740<br>hello@myhalverndental.com<br>48 Linden Crest Ave., Suite A<br>Marlow Bay, CA 90410</div>
      <div class="map" role="img" aria-label="Street map showing the clinic location"></div>
    </div>
  </div>
</section>
<footer class="footer">© 2021 Halvern Dental. All Rights Reserved</footer>
</body>
</html>
```